Giggle Stretch Joy 3 fold Brochure

a 3-fold flyer on 8.5 x 11 glossy paper showing the benefits of laughter in your life. One side should be available for mailing:
Address:
Giggle Stretch Joy
4821 Marlowe Crest
San Jose, CA 95187

other contact info:
Denise Farrow
Certified Laughter Yoga Teacher, CLYT, CLYL
info@gigglestretchjoy.example
http://gigglestretchjoy.example/Home.html
www.facebook.example/gigglestretchjoy
Blog: chucklemeadow.blogspot.example/
(408) 555-0187

Target Market(s)

non-profit organizations, medical field and corporations

Requirements
Must have
• colors as shown on the Giggle Stretch Joy web site. 3 fold flyer is to be double sided.
Should not have
• should not look too busy but needs to provide sufficient information

```html
<!DOCTYPE html>
<html lang="en">
<head>
<meta charset="utf-8">
<title>Giggle Stretch Joy – Tri-fold Brochure</title>
<link rel="stylesheet" href="https://fonts.googleapis.com/css2?family=Parisienne&family=Crimson+Text:ital,wght@0,400;0,600;1,400&family=Cinzel:wght@400;600&family=Open+Sans:wght@700;800&display=swap">
<style>
  :root {
    --purple: #8b3d9e;
    --purple-deep: #6d2a82;
    --lilac: #b98bd0;
    --lilac-pale: #e4d2ee;
    --pink: #ecb6ea;
    --lime: #c7e27c;
    --lime-deep: #8fc43c;
    --paper: #ffffff;
    --ink: #3d1f4a;
    --stage: #ece8e4;
  }
  * { box-sizing: border-box; margin: 0; padding: 0; }
  html, body { width: 1200px; height: 894px; overflow: hidden; }
  body { background: var(--stage); font-family: "Crimson Text", Georgia, serif; color: var(--ink); }

  .brochure {
    position: absolute; left: 57px; top: 27px;
    width: 1086px; height: 840px;
    display: flex;
    box-shadow: 0 6px 20px rgba(0,0,0,.18);
  }
  .panel { position: relative; width: 362px; height: 100%; overflow: hidden; background: var(--paper); }
  .panel-bg { position: absolute; inset: 0; width: 100%; height: 100%; }
  .panel-content { position: relative; z-index: 1; height: 100%; display: flex; flex-direction: column; }

  .photo { border: 3px solid var(--paper); flex: none; }

  /* Left panel */
  .banner { display: flex; height: 118px; margin: 26px 22px 0; flex: none; }
  .banner-text { width: 52%; background: var(--lime-deep); color: var(--paper); padding: 14px 10px; font-family: "Open Sans", Arial, sans-serif; }
  .banner-text .big { font-size: 34px; font-weight: 800; line-height: 1; }
  .banner-text .small { font-size: 11px; font-weight: 700; letter-spacing: .5px; }
  .banner-text .mid { font-size: 17px; font-weight: 700; }
  .banner-photo { flex: 1; background: linear-gradient(135deg, #d9c3a4, #8bb4c9 60%, #5f7f52); border: none; }
  .intro-title { margin: 22px 24px 8px; font-size: 25px; font-weight: 600; color: var(--paper); }
  .intro-copy { margin: 0 24px; font-size: 14.5px; line-height: 1.28; color: var(--paper); }
  .intro-copy + .intro-copy { margin-top: 12px; }
  .quote { margin: 20px 30px 0; font-family: "Parisienne", cursive; font-size: 25px; line-height: 1.15; color: var(--paper); text-align: center; }
  .crowd-photo { margin: auto 28px 38px; height: 178px; background: linear-gradient(160deg, #2e3b5c, #7a6e8f 45%, #c7b7a3); }

  /* Middle panel */
  .brand-mark { margin: 40px auto 0; width: 190px; height: 190px; border-radius: 50%; background: var(--purple); display: flex; align-items: center; justify-content: center; text-align: center; flex: none; }
  .brand-mark span { font-weight: 600; font-size: 26px; line-height: 1.1; color: var(--paper); }
  .contact-heading { margin: 40px 0 0 96px; font-family: "Cinzel", serif; font-weight: 600; font-size: 17px; color: var(--purple-deep); }
  .contact-block { margin: 40px 30px 0 60px; text-align: center; }
  .contact-brand { font-family: "Parisienne", cursive; font-size: 23px; color: var(--purple); }
  .contact-name { font-family: "Cinzel", serif; font-size: 17px; font-weight: 600; margin-top: 6px; }
  .contact-title { font-style: italic; font-size: 13.5px; line-height: 1.2; }
  .contact-list { list-style: none; margin: 30px 0 0 36px; font-family: "Cinzel", serif; font-size: 12px; }
  .contact-list li { display: flex; align-items: center; gap: 10px; margin-bottom: 14px; }
  .contact-list li.gap { margin-bottom: 34px; }
  .contact-list svg { width: 14px; height: 14px; flex: none; }
  .square { width: 13px; height: 13px; background: var(--purple); flex: none; }

  /* Right panel */
  .cover-title { margin: 62px 30px 0 0; text-align: right; font-family: "Parisienne", cursive; font-size: 52px; font-weight: 400; line-height: 1.05; color: var(--purple-deep); }
  .group-photo { margin: 44px 26px 0 64px; height: 280px; background: linear-gradient(140deg, #e7c9a9, #b07bb7 50%, #6f9d5c); }
  .mailing { margin: 60px 36px 0 0; text-align: right; font-style: normal; font-family: "Cinzel", serif; font-size: 12.5px; line-height: 1.5; color: var(--paper); }
</style>
</head>
<body>
<main class="brochure">

  <section class="panel panel-inside">
    <svg class="panel-bg" viewBox="0 0 362 840" preserveAspectRatio="none" aria-hidden="true">
      <rect width="362" height="840" fill="#e4d2ee"/>
      <polygon points="0,0 362,0 362,175 0,240" fill="#b98bd0"/>
      <polygon points="0,170 362,150 362,560 0,520" fill="#8b3d9e"/>
      <polygon points="0,520 362,560 362,600 0,600" fill="#ecb6ea"/>
      <polygon points="0,640 362,600 362,840 0,840" fill="#8b3d9e"/>
    </svg>
    <div class="panel-content">
      <div class="banner">
        <div class="banner-text">
          <div class="big">LAUGH</div>
          <div class="small">YOUR WAY TO</div>
          <div class="mid">GOOD HEALTH</div>
        </div>
        <div class="banner-photo photo" role="img" aria-label="Photo of smiling friends laughing together"></div>
      </div>
      <h2 class="intro-title">What is Laughter Yoga?</h2>
      <p class="intro-copy">Laughter Yoga was started in India in 1995 by medical doctor Dr. Ravi Mehtar as he was researching an article, “Laughter: The Best Medicine.” The laughter club began with five people in a park and has now spread to over 100 countries.</p>
      <p class="intro-copy">Laughter Yoga is a combination of deep breathing exercises and playful activities full of guided giggling that is a well-being workout that can greatly boost your energy and enhance your vitality. Just as smiling can do more for your facial muscles than frowning, imagine what a hearty belly laugh can do!</p>
      <p class="quote">Laugh out loud and<br>live life to the fullest!</p>
      <div class="crowd-photo photo" role="img" aria-label="Photo of a group laughing with arms raised during a session"></div>
    </div>
  </section>

  <section class="panel panel-contact">
    <svg class="panel-bg" viewBox="0 0 362 840" preserveAspectRatio="none" aria-hidden="true">
      <rect width="362" height="840" fill="#c7e27c"/>
      <polygon points="0,0 70,0 70,840 0,840" fill="#f6f1f8"/>
      <polygon points="70,0 362,0 362,90 70,300" fill="#ecb6ea"/>
      <polygon points="0,240 70,300 70,840 0,840" fill="#e4d2ee"/>
    </svg>
    <div class="panel-content">
      <div class="brand-mark"><span>Giggle<br>Stretch Joy</span></div>
      <h3 class="contact-heading">CONTACT US:</h3>
      <div class="contact-block">
        <div class="contact-brand">Giggle Stretch Joy</div>
        <div class="contact-name">Denise Farrow</div>
        <div class="contact-title">Certified Laughter Yoga Teacher,<br>CLYT, CLYL</div>
      </div>
      <ul class="contact-list">
        <li><svg viewBox="0 0 14 14"><path d="M7 1 1 6.5h2V13h3V9h2v4h3V6.5h2z" fill="#3d1f4a"/></svg>4821 Marlowe Crest, San Jose, CA 95187</li>
        <li class="gap"><svg viewBox="0 0 14 14"><path d="M3 1h3l1 3-2 1.5a8 8 0 0 0 3.5 3.5L10 7l3 1v3a2 2 0 0 1-2 2A10 10 0 0 1 1 3a2 2 0 0 1 2-2z" fill="#3d1f4a"/></svg>(408) 555-0187</li>
        <li><svg viewBox="0 0 14 14"><circle cx="7" cy="7" r="6" fill="none" stroke="#3d1f4a" stroke-width="1.4"/><path d="M1 7h12M7 1c-3 3-3 9 0 12M7 1c3 3 3 9 0 12" fill="none" stroke="#3d1f4a"/></svg>www.gigglestretchjoy.example</li>
        <li><svg viewBox="0 0 14 14"><rect x="1" y="3" width="12" height="8" fill="none" stroke="#3d1f4a" stroke-width="1.4"/><path d="m1 3 6 5 6-5" fill="none" stroke="#3d1f4a" stroke-width="1.2"/></svg>info@gigglestretchjoy.example</li>
        <li><span class="square"></span>/gigglestretchjoy</li>
        <li><span class="square"></span>chucklemeadow.blogspot.example/</li>
      </ul>
    </div>
  </section>

  <section class="panel panel-cover">
    <svg class="panel-bg" viewBox="0 0 362 840" preserveAspectRatio="none" aria-hidden="true">
      <rect width="362" height="840" fill="#e4d2ee"/>
      <polygon points="0,0 362,0 362,60 0,270" fill="#8b3d9e"/>
      <polygon points="362,60 362,330 180,240" fill="#b98bd0"/>
      <polygon points="0,270 60,320 0,520" fill="#c7e27c"/>
      <polygon points="0,560 362,470 362,840 0,840" fill="#8b3d9e"/>
      <polygon points="0,560 200,510 0,700" fill="#b98bd0"/>
    </svg>
    <div class="panel-content">
      <h1 class="cover-title">Giggle<br>Stretch Joy</h1>
      <div class="group-photo photo" role="img" aria-label="Photo of a group lying in a circle laughing"></div>
      <address class="mailing">
        4821 Marlowe Crest, San Jose, CA 95187<br>
        www.gigglestretchjoy.example<br>
        (408) 555-0187
      </address>
    </div>
  </section>

</main>
</body>
</html>
```